MORVELA silk scarf packaging

Packaging options needed for silk scarves/twillies as well as gold plated accesory (used to secure a scarf). Scarf has to be packaged together with accesory.
There are two sizes of scarves:
85x5cm small twilly
90x90 cm regular scarf size
Scarf accesory :
4,5x2x1,8 cm gold plated branded
There will be various scarf designs going forward. Currently most scarves are created using baltic folk patterns and two twillies (85x5cm) designs are based on watercolor art patterns. Daring, out-of-the-box thinking, visible and eye catching packaging ideas are welcome.

```html
<!DOCTYPE html>
<html lang="en">
<head>
<meta charset="utf-8">
<title>MORVELA – Small Scarf Envelope, Outer and Inner</title>
<link rel="stylesheet" href="https://fonts.googleapis.com/css2?family=Inter:wght@300;400&family=Open+Sans:wght@400&display=swap">
<style>
  :root {
    --paper: #ffffff;
    --ink: #000000;
    --mint: #9fd4cf;
    --gold: #d8c07a;
    --pointer: #1fa3e0;
    --clasp-tint: #e6e3d6;
    --ribbon-tint: #e9ecec;
  }
  html, body {
    margin: 0;
    padding: 0;
    overflow: hidden;
    background: var(--paper);
  }
  .sheet {
    display: block;
    width: 1200px;
    height: 734px;
  }
  .view-label {
    font-family: "Open Sans", sans-serif;
    font-size: 25px;
    fill: var(--ink);
  }
  .dimension-label {
    font-family: "Inter", sans-serif;
    font-size: 9px;
    letter-spacing: 1.5px;
    fill: var(--ink);
  }
  .dimension-line { stroke: var(--ink); stroke-width: 0.8; fill: none; }
  .outer-panel { fill: var(--ink); }
  .outer-frame { fill: none; stroke: var(--mint); stroke-width: 3; }
  .brand-band {
    font-family: "Inter", sans-serif;
    font-weight: 300;
    font-size: 44px;
    fill: var(--mint);
  }
  .brand-centre {
    font-family: "Inter", sans-serif;
    font-weight: 300;
    font-size: 12px;
    letter-spacing: 3px;
    fill: var(--mint);
  }
  .closure-slot { stroke: var(--paper); stroke-width: 1; fill: none; }
  .closure-notch { fill: var(--paper); }
  .accessory-pointer { stroke: var(--pointer); stroke-width: 0.8; }
  .accessory-art { fill: var(--gold); }
  .inner-panel { fill: var(--mint); stroke: var(--ink); stroke-width: 0.8; }
  .inner-fold { fill: none; stroke: var(--ink); stroke-width: 0.8; }
  .ribbon-art { fill: var(--ribbon-tint); }
  .clasp-art { fill: var(--clasp-tint); }
</style>
</head>
<body>
<svg class="sheet" viewBox="0 0 1200 734" xmlns="http://www.w3.org/2000/svg">

  <!-- Outer side of the envelope -->
  <g class="outer-view">
    <text class="view-label" x="71" y="70">Small Outer</text>
    <text class="view-label" x="30" y="266">accessory</text>
    <line class="accessory-pointer" x1="60" y1="281" x2="69" y2="362"/>

    <path class="outer-panel" d="M286,98 L287,81 Q288,74 295,74 L323,74 Q330,74 331,81 L332,98 Z"/>
    <path class="outer-panel" d="M188,262 L205,115 Q207,99 222,99 L402,99 Q417,99 418,115 L433,262 Z"/>
    <path class="outer-panel" d="M188,506 L433,506 L418,630 Q416,645 401,645 L220,645 Q205,645 203,630 Z"/>
    <path class="outer-panel" d="M188,262 L172,262 Q166,262 160,267 L46,366 Q38,374 38,383 Q38,393 46,400 L160,498 Q166,506 172,506 L188,506 Z"/>
    <path class="outer-panel" d="M433,262 L450,262 Q456,262 462,267 L576,366 Q584,374 584,383 Q584,393 576,400 L462,498 Q456,506 450,506 L433,506 Z"/>
    <rect class="outer-panel" x="188" y="262" width="245" height="244"/>
    <rect class="outer-frame" x="190" y="264" width="241" height="240"/>

    <text class="brand-centre" x="312" y="388" text-anchor="middle">MORVELA</text>
    <text class="brand-band" x="310" y="496" text-anchor="middle" textLength="224" lengthAdjust="spacingAndGlyphs">MORVELA</text>

    <line class="closure-slot" x1="284" y1="594" x2="287" y2="590"/>
    <line class="closure-slot" x1="287" y1="590" x2="331" y2="590"/>
    <line class="closure-slot" x1="331" y1="590" x2="334" y2="594"/>
    <path class="closure-notch" d="M301,590 A8,8 0 0 0 317,590 Z"/>

    <rect class="accessory-art" x="61" y="362" width="111" height="39" rx="18" role="img" aria-label="Gold plated scarf accessory, open U-shaped clasp halves"/>

    <line class="dimension-line" x1="188" y1="670" x2="430" y2="670"/>
    <line class="dimension-line" x1="188" y1="663" x2="188" y2="677"/>
    <line class="dimension-line" x1="430" y1="663" x2="430" y2="677"/>
    <text class="dimension-label" x="334" y="690" text-anchor="middle">10cm</text>
  </g>

  <!-- Inner side of the envelope -->
  <g class="inner-view">
    <text class="view-label" x="587" y="233">Small Inner</text>

    <g role="img" aria-label="Repeating diagonal brand-name pattern in white on mint">
      <path class="inner-panel" d="M873,94 L874,76 Q875,69 882,69 L913,69 Q920,69 921,76 L922,94 Z"/>
      <path class="inner-panel" d="M777,258 L793,110 Q795,94 810,94 L990,94 Q1005,94 1007,110 L1022,258 Z"/>
      <path class="inner-panel" d="M777,503 L1022,503 L1006,627 Q1004,642 989,642 L809,642 Q794,642 792,627 Z"/>
      <path class="inner-panel" d="M777,258 L762,258 Q756,258 750,263 L633,366 Q625,373 625,380 Q625,388 633,395 L750,498 Q756,503 762,503 L777,503 Z"/>
      <path class="inner-panel" d="M1022,258 L1036,258 Q1042,258 1048,263 L1166,366 Q1174,373 1174,380 Q1174,388 1166,395 L1048,498 Q1042,503 1036,503 L1022,503 Z"/>
      <rect class="inner-panel" x="777" y="258" width="245" height="245"/>
    </g>
    <rect class="inner-fold" x="777" y="258" width="245" height="245"/>

    <ellipse class="ribbon-art" cx="720" cy="380" rx="20" ry="33" role="img" aria-label="Curved ribbon loop holding the twilly"/>
    <rect class="clasp-art" x="1083" y="357" width="19" height="36" role="img" aria-label="Slot holding the gold scarf clasp"/>

    <line class="dimension-line" x1="615" y1="262" x2="615" y2="504"/>
    <line class="dimension-line" x1="608" y1="262" x2="622" y2="262"/>
    <line class="dimension-line" x1="608" y1="504" x2="622" y2="504"/>
    <text class="dimension-label" x="586" y="318" text-anchor="middle">10cm</text>
  </g>
</svg>
</body>
</html>
```